Backup Software Tri-fold Brochure Project

We need a great looking and informative brochure to describe our new Backup Software offering. The brochures are to be used in retail and small business environments given to clients interested in protecting their computer from data loss.
The brochure should include attractive imagery that conveys a sense of Trust and Security to the prospective client.
The copy is provided as an attachment to this project. We'd like our Bright Deskpoint product logo to be printed on the back cover. The logo is attached to this project.
The finished tri-fold brochure will be submitted to Plumcopy for printing as an 8.5" x 11" tri-fold brochure. Their design instructions are online http://plumcopy-example.com/custom-brochures.aspx.
The finished product should be Adobe Illustrator CS3 (*.ai) with a PDF Proof.
Target Market(s)
Retail and Small Business customers
Industry/Entity Type
Software
Designer to choose colors to be used in the design.

```html
<!DOCTYPE html>
<html lang="en">
<head>
<meta charset="utf-8">
<title>Bright Deskpoint – Tri-fold Brochure Outside</title>
<link rel="stylesheet" href="https://fonts.googleapis.com/css2?family=Roboto+Condensed:wght@400;700&family=Ubuntu:wght@400;700&display=swap">
<style>
  :root {
    --navy: #2e3274;
    --navy-deep: #262a63;
    --green: #6c9d3f;
    --green-text: #7dbb45;
    --grey: #d5d6dc;
    --paper: #ececef;
    --backdrop: #e4e4e6;
    --white: #ffffff;
    --globe-a: #5d68a8;
    --globe-b: #3a4287;
  }
  * { box-sizing: border-box; margin: 0; padding: 0; }
  html, body {
    width: 1200px; height: 800px; overflow: hidden;
    background: var(--backdrop);
  }
  .brochure {
    position: absolute; left: 105px; top: 18px;
    width: 990px; height: 765px;
    box-shadow: 0 6px 18px rgba(0,0,0,.18);
    overflow: hidden;
  }
  .brochure__art { position: absolute; inset: 0; }
  .panel { position: absolute; top: 0; width: 330px; height: 765px; }
  .panel--inside-flap { left: 0; }
  .panel--back { left: 330px; }
  .panel--cover { left: 660px; }

  .risk-copy {
    position: absolute; left: 34px; top: 300px; width: 268px;
    font-family: "Ubuntu", sans-serif; color: var(--white);
    font-size: 11.2px; line-height: 1.36; text-align: justify;
  }
  .risk-copy__title {
    font-family: "Roboto Condensed", sans-serif; font-weight: 700;
    color: var(--green-text); font-size: 15px; letter-spacing: .3px;
    margin-bottom: 6px;
  }
  .risk-copy p + p { margin-top: 14px; }

  .brand {
    position: absolute; display: flex; align-items: center; gap: 10px;
    font-family: "Ubuntu", sans-serif; font-weight: 700;
    color: var(--green-text); font-size: 26px; line-height: 1;
    text-transform: uppercase; letter-spacing: .5px;
  }
  .brand__mark { width: 22px; height: 22px; background: var(--green-text); flex: none; }
  .panel--back .brand { left: 40px; top: 430px; }
  .panel--cover .brand { left: 50px; top: 250px; }

  .contact-list {
    position: absolute; left: 40px; top: 520px; list-style: none;
    font-family: "Roboto Condensed", sans-serif; font-weight: 700;
    color: var(--green-text); font-size: 13px; line-height: 1.3;
  }
  .contact-list li { display: flex; align-items: center; gap: 16px; margin-bottom: 18px; }
  .contact-list svg { width: 28px; height: 28px; flex: none; }

  .cover-visual {
    position: absolute; left: 18px; top: 330px;
    width: 300px; height: 300px; border-radius: 50%;
    border: 7px solid var(--grey);
    background: radial-gradient(circle at 50% 45%, var(--globe-a), var(--globe-b));
  }
</style>
</head>
<body>
<main class="brochure">
  <svg class="brochure__art" viewBox="0 0 990 765" aria-hidden="true">
    <!-- inside flap -->
    <rect x="0" y="0" width="330" height="765" fill="var(--navy)"/>
    <polygon points="0,0 330,0 330,60 0,250" fill="var(--green)"/>
    <polygon points="0,0 200,0 0,120" fill="var(--grey)"/>
    <polygon points="330,300 330,765 40,765" fill="var(--green)"/>
    <rect x="140" y="150" width="120" height="120" fill="var(--grey)" transform="rotate(12 200 210)"/>
    <rect x="200" y="130" width="80" height="80" fill="none" stroke="var(--white)" stroke-width="1.5" transform="rotate(8 240 170)"/>
    <!-- back panel -->
    <rect x="330" y="0" width="330" height="765" fill="var(--navy)"/>
    <path d="M600,0 L660,0 L660,40 Q520,180 330,360 L330,300 Q500,150 600,0 Z" fill="var(--green)"/>
    <path d="M660,40 L660,300 Q560,300 480,330 Q560,170 660,40 Z" fill="var(--grey)"/>
    <rect x="470" y="160" width="90" height="80" fill="var(--grey)" transform="rotate(10 515 200)"/>
    <rect x="500" y="70" width="55" height="55" fill="none" stroke="var(--white)" stroke-width="1.5" transform="rotate(15 527 97)"/>
    <rect x="395" y="50" width="60" height="60" fill="none" stroke="var(--white)" stroke-width="1.5" transform="rotate(20 425 80)"/>
    <!-- cover -->
    <rect x="660" y="0" width="330" height="765" fill="var(--paper)"/>
    <polygon points="660,0 760,0 990,170 990,260 660,40" fill="var(--green)"/>
    <polygon points="860,0 990,0 990,150" fill="var(--navy)"/>
    <polygon points="760,0 790,0 990,150 990,175" fill="var(--navy)"/>
    <path d="M660,300 Q760,580 990,650 L990,765 L660,765 Z" fill="var(--navy)"/>
    <rect x="680" y="40" width="70" height="60" fill="none" stroke="var(--white)" stroke-width="1.5" transform="rotate(15 715 70)"/>
    <rect x="905" y="40" width="60" height="55" fill="var(--grey)" transform="rotate(10 935 67)"/>
    <rect x="890" y="110" width="60" height="55" fill="none" stroke="var(--white)" stroke-width="1.5" transform="rotate(10 920 137)"/>
    <!-- folds -->
    <line x1="330" y1="0" x2="330" y2="765" stroke="rgba(0,0,0,.12)"/>
    <line x1="660" y1="0" x2="660" y2="765" stroke="rgba(0,0,0,.12)"/>
  </svg>

  <section class="panel panel--inside-flap">
    <div class="risk-copy">
      <h2 class="risk-copy__title">YOUR ENTIRE DIGITAL LIFE IS AT RISK</h2>
      <p>Your computer stores everything you’ve ever created. Everything you’ve written, every email you’ve sent, every list you’ve made, every picture you’ve taken or movie you’ve made, all music you’ve created, your proposals, your spreadsheets, your presentations, your word files, your artwork, programs you’ve written, anything you’ve dictated, and much more… All your digital life is stored on your computer and is at risk of loss without backup.</p>
      <p>And your computer stores a copy of all your personal information. Your passwords, your online banking, your PINs, your credit cards and all your health and shopping records. This makes it a juicy target for hackers. Every day your digital life is exposed to computer Viruses, Malware and spammers all trying to break in. If they succeed the damage could be incalculable.</p>
      <p>If hackers destroy your information or a simple hard drive failure happens, restoring your programs will cost you days of effort and potentially hundreds of dollars. But your files could be unrecoverable. This means the loss of everything you’ve ever created. The only protection is a great backup.</p>
    </div>
  </section>

  <section class="panel panel--back">
    <div class="brand"><span class="brand__mark"></span>Bright Deskpoint</div>
    <ul class="contact-list">
      <li>
        <svg viewBox="0 0 28 28"><circle cx="14" cy="14" r="13" fill="none" stroke="var(--green-text)" stroke-opacity=".5"/><rect x="8" y="10" width="12" height="8" fill="none" stroke="var(--green-text)"/><path d="M8 10 L14 15 L20 10" fill="none" stroke="var(--green-text)"/></svg>
        <span>INFO@BRIGHTDESKPOINT-EXAMPLE.COM</span>
      </li>
      <li>
        <svg viewBox="0 0 28 28"><circle cx="14" cy="14" r="13" fill="none" stroke="var(--green-text)" stroke-opacity=".5"/><path d="M10 8 L12 8 L13 11 L11.5 12.5 Q13 15.5 15.5 16.5 L17 15 L20 16 L20 18 Q18 20 15 19 Q10 17 9 12 Q9 9 10 8 Z" fill="var(--green-text)"/></svg>
        <span>+00 1234 5678 3012<br>+00 1234 5678 3012</span>
      </li>
      <li>
        <svg viewBox="0 0 28 28"><circle cx="14" cy="14" r="13" fill="none" stroke="var(--green-text)" stroke-opacity=".5"/><path d="M8 14 L14 8 L20 14 L18 14 L18 19 L10 19 L10 14 Z" fill="var(--green-text)"/></svg>
        <span>YOUR CITY ADDRESS<br>STREET LOCATION, YOUR CITY, COUNTRY.</span>
      </li>
      <li>
        <svg viewBox="0 0 28 28"><circle cx="14" cy="14" r="13" fill="none" stroke="var(--green-text)" stroke-opacity=".5"/><circle cx="14" cy="14" r="6" fill="none" stroke="var(--green-text)"/><path d="M8 14 H20 M14 8 Q11 14 14 20 M14 8 Q17 14 14 20" fill="none" stroke="var(--green-text)"/></svg>
        <span>WWW.BRIGHTDESKPOINT-EXAMPLE.COM</span>
      </li>
    </ul>
  </section>

  <section class="panel panel--cover">
    <div class="brand"><span class="brand__mark"></span>Bright Deskpoint</div>
    <div class="cover-visual" role="img" aria-label="World map with a laptop showing a padlock, symbolising secure backup"></div>
  </section>
</main>
</body>
</html>
```